Use monitor (event monitor)

I have developed an eventmonitor for firestations for about 2 years. now i want a redesign of this montor. i have 2 views - defaultView and alarmView. the default view shows the firestation. the cars from the firestations if they are out of order or not, a view from the actual weather, and the last firealarms of our country. The alarmview. Shows specific information about the place where a fire, or a firestation is needed. it shows on openstreetmap the positions of cars, and additional information. I want to redesign this 2 sites. ideas to look at the monitor more beautiful. for the alarmview maybe new ideas how to display the cars in the map, and maybe a better place for postioning. i want upload actual 2 images that people get a feeling for that. the monitor is mostly used with a tv or a monitor. when the people are in the firestation, they want to see the needed information. what happens, where when ..... Hope this is enough information

```html
<!DOCTYPE html>
<html lang="de">
<head>
<meta charset="utf-8">
<title>Feuerwehr Falkenau – Einsatzmonitor</title>
<link rel="stylesheet" href="https://fonts.googleapis.com/css2?family=Oswald:wght@600&family=Roboto:wght@400;500&display=swap">
<style>
  :root {
    --brand-red: #c10006;
    --row-red: #c4000a;
    --white: #ffffff;
    --row-grey: #e8e8e8;
    --text-dark: #2b2b2b;
    --panel-dark: rgba(22, 24, 26, 0.88);
    --panel-border: #8c8c8c;
    --bg-top: #3b4046;
    --bg-mid: #2c3a2a;
    --bg-bottom: #1f2d1c;
  }
  * { box-sizing: border-box; margin: 0; padding: 0; }
  html, body { width: 1200px; height: 991px; overflow: hidden; }
  body {
    position: relative;
    font-family: "Roboto", Arial, sans-serif;
    color: var(--text-dark);
    background: var(--bg-bottom);
  }
  .backdrop {
    position: absolute; inset: 0;
    background: linear-gradient(180deg, var(--bg-top) 0%, #343b34 35%, var(--bg-mid) 65%, var(--bg-bottom) 100%);
  }
  .topbar {
    position: absolute; left: 0; top: 0; width: 1200px; height: 62px;
    background: var(--brand-red);
  }
  .station-name {
    position: absolute; left: 54px; top: 10px;
    font-family: "Oswald", "Arial Narrow", sans-serif; font-weight: 600;
    font-size: 29px; color: var(--white); letter-spacing: 0.2px;
  }
  .clock {
    position: absolute; right: 59px; top: 18px;
    font-size: 14px; color: var(--white);
  }
  .gauge {
    position: absolute; top: 97px; height: 82px; width: 540px;
    background: var(--panel-dark); border: 1px solid var(--panel-border);
    color: var(--white); text-align: center; font-size: 21px; line-height: 29px;
    padding-top: 11px;
  }
  .gauge--left { left: 55px; }
  .gauge--right { left: 601px; }
  .alarm-board {
    position: absolute; left: 54px; top: 207px; width: 744px; height: 666px;
    background: var(--white); border-radius: 3px; overflow: hidden;
  }
  .alarm-row {
    position: relative; height: 48.5px; font-size: 12px; font-weight: 500;
  }
  .alarm-row:nth-child(even) { background: var(--row-grey); }
  .alarm-list { border-bottom: 1px solid #bdbdbd; }
  .alarm-row span { position: absolute; top: 17px; white-space: nowrap; }
  .c-date { left: 34px; }
  .c-time { left: 159px; }
  .c-unit { left: 261px; }
  .c-type { left: 414px; top: 15px !important; }
  .c-place { left: 599px; }
  .region-map {
    position: absolute; left: 221px; top: 466px; width: 296px; height: 166px;
  }
  .fleet {
    position: absolute; left: 813px; top: 207px; width: 328px;
  }
  .fleet-row {
    position: relative; height: 48.5px; font-size: 12px; font-weight: 500;
    background: var(--white); color: var(--text-dark);
  }
  .fleet-row:nth-child(odd) { background: var(--row-red); color: var(--white); }
  .fleet-row span { position: absolute; }
  .f-name { left: 39px; top: 18px; }
  .f-state { left: 205px; top: 16px; }
  .footer {
    position: absolute; left: 0; width: 1200px; top: 937px;
    text-align: center; color: var(--white); font-size: 15px;
  }
</style>
</head>
<body>
  <div class="backdrop" role="img" aria-label="Luftaufnahme einer grünen Tallandschaft mit Dorf und Fluss, abgedunkelt"></div>

  <header class="topbar">
    <div class="station-name">Feuerwehr Falkenau</div>
    <div class="clock">Sonntag, 29. Jan. 2017, 13:33</div>
  </header>

  <section class="gauge gauge--left">Wasserstand Grünbach<br>149cm</section>
  <section class="gauge gauge--right">Wasserstand Kirchau<br>106cm</section>

  <main class="alarm-board">
    <div class="alarm-list">
      <div class="alarm-row"><span class="c-date">29.1.2017</span><span class="c-time">13:06</span><span class="c-unit">FW Almsee</span><span class="c-type">Eigenanforderung</span><span class="c-place">6065 Almsee</span></div>
      <div class="alarm-row"><span class="c-date">29.1.2017</span><span class="c-time">12:47</span><span class="c-unit">FW Bergtal</span><span class="c-type">Technischer Einsatz</span><span class="c-place">6100 Bergtal/Nord</span></div>
      <div class="alarm-row"><span class="c-date">29.1.2017</span><span class="c-time">11:58</span><span class="c-unit">FW Kornau</span><span class="c-type">Eigenanforderung</span><span class="c-place">6114 Kornau</span></div>
      <div class="alarm-row"><span class="c-date">29.1.2017</span><span class="c-time">11:25</span><span class="c-unit">FW Wies/Lindtal</span><span class="c-type">Eigenanforderung</span><span class="c-place">6182 Wies/Lindtal</span></div>
      <div class="alarm-row"><span class="c-date">29.1.2017</span><span class="c-time">10:30</span><span class="c-unit">FW Hochwald</span><span class="c-type">Nachalarmierung</span><span class="c-place">6647 Felsach</span></div>
      <div class="alarm-row"><span class="c-date">29.1.2017</span><span class="c-time">10:30</span><span class="c-unit">FW Moosbach</span><span class="c-type">Unterstutzungseinsatz</span><span class="c-place">6647 Felsach</span></div>
      <div class="alarm-row"><span class="c-date">29.1.2017</span><span class="c-time">10:03</span><span class="c-unit">FW Birkenwangle</span><span class="c-type">Eigenanforderung</span><span class="c-place">6672 Birkenwangle</span></div>
      <div class="alarm-row"><span class="c-date">29.1.2017</span><span class="c-time">10:00</span><span class="c-unit">FW Eichdorf-Tamant</span><span class="c-type">OL Eigenanforderung</span><span class="c-place">9990 Eichdorf-Tamant</span></div>
      <div class="alarm-row"><span class="c-date">29.1.2017</span><span class="c-time">09:44</span><span class="c-unit">FW Lärchtal</span><span class="c-type">Eigenanforderung</span><span class="c-place">6105 Lärchtal</span></div>
    </div>
    <svg class="region-map" role="img" aria-label="Regionalkarte mit eingefärbten Bezirken und Fahrzeugsymbolen je Einsatzgebiet" viewBox="0 0 296 166">
      <defs>
        <linearGradient id="mapTone" x1="0" y1="0" x2="1" y2="1">
          <stop offset="0" stop-color="#e8666b"/>
          <stop offset="1" stop-color="#c4000a"/>
        </linearGradient>
      </defs>
      <rect x="0" y="0" width="296" height="166" rx="6" fill="url(#mapTone)"/>
    </svg>
  </main>

  <aside class="fleet">
    <div class="fleet-row"><span class="f-name">FF Florian</span><span class="f-state">Frei auf Wache</span></div>
    <div class="fleet-row"><span class="f-name">KDOF-1</span><span class="f-state">Frei auf Wache</span></div>
    <div class="fleet-row"><span class="f-name">LF-1</span><span class="f-state">Frei auf Wache</span></div>
    <div class="fleet-row"><span class="f-name">RLF-1</span><span class="f-state">Frei auf Wache</span></div>
    <div class="fleet-row"><span class="f-name">MTF-1</span><span class="f-state">Frei auf Wache</span></div>
    <div class="fleet-row"><span class="f-name">BOOT-1</span><span class="f-state">Frei auf Wache</span></div>
    <div class="fleet-row" style="height:43px"><span class="f-name">BOOT-2</span><span class="f-state">Frei auf Wache</span></div>
  </aside>

  <footer class="footer">Copyright © 2018. All Rights Reserved - Privacy Policy</footer>
</body>
</html>
```